Flyer für einen ambulanten Pflegedienst
Zielgruppe
Wir sind ein ambulanter Pflegedienst und suchen ansprechende Designs und Vorlagen für unsere Flyer. Die Zielgruppe sind pflegebedürftige ältere Menschen und deren Angehörigen. Die Flyer sollen in Briefkästen, bei Ärzten, Krankenhäusern, Physiotherapiepraxen etc. verteilt werden.
Aufgabenstellung
Ich bin offen für Vorschläge und habe keine bestimmten Vorstellungen.

```html
<!DOCTYPE html>
<html lang="de">
<head>
<meta charset="utf-8">
<title>Pflegedienst Wegbegleiter – Flyer</title>
<link rel="stylesheet" href="https://fonts.googleapis.com/css2?family=Fira+Sans:wght@400;700&family=Open+Sans:ital,wght@0,400;0,700;1,400&family=Dancing+Script:wght@600&display=swap">
<style>
  :root{
    --green:#0c8a5c;
    --green-soft:#7cc49a;
    --green-mid:#bfdcc9;
    --green-pale:#ecf5ef;
    --grey-pale:#e4e4e4;
    --ink:#2b2b2b;
    --paper:#ffffff;
  }
  *{margin:0;padding:0;box-sizing:border-box}
  html,body{width:848px;height:1200px;overflow:hidden;background:var(--paper)}
  .canvas{position:relative;width:848px;height:1200px}
  .flyer{position:absolute;top:210px;width:390px;height:780px;background:var(--paper);overflow:hidden;border:1px solid #ececec}
  .flyer--front{left:22px;font-family:"Fira Sans",sans-serif}
  .flyer--back{left:436px;font-family:"Open Sans",sans-serif;color:var(--ink)}
  .disc{position:absolute;border-radius:50%}
  .photo{position:absolute;border-radius:50%}

  /* front */
  .tagline{position:absolute;left:29px;top:34px;font-size:16px;color:var(--green)}
  .brand{position:absolute;left:29px;top:92px;display:flex;align-items:center;gap:12px}
  .brand__dot{width:44px;height:44px;border-radius:50%;background:var(--green)}
  .brand__name{font-weight:700;font-size:34px;line-height:36px;color:var(--green)}
  .claim-box{position:absolute;left:196px;top:184px;width:194px;height:98px;background:var(--green-soft);color:#fff;font-size:13.4px;line-height:20.5px;padding:9px 0 0 11px;letter-spacing:.2px}
  .web-front{position:absolute;left:29px;top:724px;font-size:19px;font-weight:700;color:var(--ink);letter-spacing:.2px}

  /* back */
  .services{position:absolute;right:24px;top:44px;text-align:right;font-size:13.5px;line-height:18.5px}
  .promise{position:absolute;left:160px;top:128px;width:222px;font-weight:700;font-size:13.4px;line-height:17.5px;color:var(--green)}
  .body-copy{position:absolute;left:42px;top:274px;font-size:11.6px;line-height:16px}
  .goal{position:absolute;left:40px;top:446px;font-weight:700;font-size:12.5px;line-height:17px}
  .info{position:absolute;left:40px;top:540px;font-style:italic;font-size:11.4px;line-height:17px}
  .info__phone{font-style:normal;font-weight:700;color:var(--green);font-size:13px}
  .slogan{position:absolute;left:40px;top:612px;font-weight:700;font-size:15px}
  .greeting{position:absolute;left:70px;top:640px;font-family:"Dancing Script",cursive;font-size:28px;color:var(--green);white-space:nowrap}
  .address{position:absolute;left:30px;top:716px;font-size:10px;line-height:14px;white-space:nowrap}
  .address__name{font-weight:700;color:var(--green)}
  .contact{position:absolute;left:178px;top:732px;font-size:9px;line-height:13px;white-space:nowrap}
  .web-vertical{position:absolute;left:371px;top:627px;transform:translate(-50%,-50%) rotate(-90deg);font-weight:700;font-size:13px;white-space:nowrap}
</style>
</head>
<body>
<div class="canvas">

  <section class="flyer flyer--front">
    <div class="disc" style="left:-80px;top:309px;width:372px;height:372px;background:var(--green-pale)"></div>
    <div class="disc" style="left:300px;top:490px;width:208px;height:208px;background:var(--grey-pale)"></div>
    <div class="photo" role="img" aria-label="Foto: Pflegekraft legt einer lächelnden älteren Dame die Hand auf die Schulter" style="left:44px;top:245px;width:298px;height:298px;background:radial-gradient(circle at 65% 40%,#c98a6c 0%,#8f9a7a 40%,#7d8a92 75%,#6f7f86 100%)"></div>
    <div class="disc" style="left:151px;top:473px;width:112px;height:112px;background:var(--green-mid);opacity:.85"></div>
    <p class="tagline">Ihr Wohl an erster Stelle</p>
    <div class="brand">
      <span class="brand__dot"></span>
      <span class="brand__name">Pflegedienst<br>Wegbegleiter</span>
    </div>
    <p class="claim-box">Wir sind ein verlässlicher<br>Partner für individuelle,<br>professionelle ambulante<br>Pflege im Raum Frankfurt</p>
    <p class="web-front">pflegedienst-wegbegleiter.de</p>
  </section>

  <section class="flyer flyer--back">
    <div class="disc" style="left:116px;top:116px;width:196px;height:196px;background:var(--green-pale)"></div>
    <div class="disc" style="left:182px;top:38px;width:70px;height:70px;background:var(--grey-pale)"></div>
    <div class="disc" style="left:276px;top:480px;width:110px;height:110px;background:var(--grey-pale)"></div>
    <div class="disc" style="left:350px;top:340px;width:70px;height:70px;background:var(--green-pale)"></div>
    <div class="disc" style="left:-70px;top:520px;width:150px;height:150px;background:#f0f0f0"></div>
    <div class="photo" role="img" aria-label="Foto: Ärztin bespricht mit einem älteren Herrn Unterlagen auf dem Sofa" style="left:-14px;top:3px;width:180px;height:180px;background:radial-gradient(circle at 50% 45%,#e9e4dc 0%,#b9ad96 45%,#6b6a6e 100%)"></div>
    <div class="photo" role="img" aria-label="Foto: Pflegerin begleitet eine ältere Dame im Wohnzimmer" style="left:262px;top:372px;width:140px;height:140px;background:radial-gradient(circle at 55% 45%,#d6dde3 0%,#8fb0c9 40%,#7a6f66 100%)"></div>

    <p class="services">Grundpflege<br>häusliche Betreuung<br>hauswirtschaftliche Hilfe<br>Pflegeberatung</p>
    <p class="promise">Wir erhalten und fördern die<br>Selbstständigkeit unserer<br>Patienten und berücksichtigen<br>ihre individuellen körperlichen,<br>psychologischen und kultu-<br>rellen Bedürfnisse.</p>
    <p class="body-copy">Dabei schaffen wir eine vertrauensvolle Atmosphäre, in<br>der sich unsere Klienten sicher und gut aufgehoben fühlen.<br>Mit Respekt, Professionalität und Einfühlungsvermögen<br>begleiten wir unsere Patienten zuverlässig in jeder<br>Lebensphase – von der Unterstützung im<br>Alltag bis zur einfühlsamen Begleitung in<br>schwierigen Momenten. Wir bieten Ihnen<br>individuelle Pflege und Betreuung in Ihrer<br>gewohnten Häuslichkeit.</p>
    <p class="goal">Unser Ziel ist es, Sie dabei<br>zu unterstützen, so lange wie<br>möglich selbstständig und sicher<br>in Ihrem Zuhause zu leben.</p>
    <p class="info">Mehr Informationen erhalten Sie<br>auf unserer Webseite oder vereinbaren<br>Sie einen Termin mit uns. Tel.: <span class="info__phone">069 58214470</span></p>
    <p class="slogan">Ihr Wohl an erster Stelle</p>
    <p class="greeting">Wir freuen uns auf Sie.</p>
    <p class="address"><span class="address__name">Pflegedienst Wegbegleiter</span><br>Lindenweg 12<br>60313 Frankfurt am Main</p>
    <p class="contact">Telefon: +49 69 58214470<br>E-Mail: info@pflegedienst-wegbegleiter.de<br>Bürozeiten: 08:00 - 14:00 Uhr</p>
    <p class="web-vertical">pflegedienst-wegbegleiter.de</p>
  </section>

</div>
</body>
</html>
```